Simple Supplement Protein Bag design

We are looking for a simple, professional, clean bag design for a line of supplements.
Our logo and the packaging template can be seen in the attachments.

We want to use Blues, light blues and white

can possible include black and/or silver.
or black and white.

Our logo can be in black or blue.

Ive attached some similar bag designs we like.

The bag will be used for a range of products, protein powders, weightgainers etc.. but it will be a generic design for all of the products.

The brand is VITALPRADERA.EXAMPLE.CO and the line of products is called "Tundra Range"

The design will be very simple with the brand name, tundra range and 3 small logos with text (as indicated in file "DRAWING" attached)

Surrounding the 3 small logos will be the text (in english on top, and spanish below)

1: quality guaranteed
calidad garantizada

2: imported ingredients
materias primas importadas

3: good manufacturing practices
buenas practicas de manufactura

We are looking for bag design , images and template for printing.

The files attached are:

1 and DRAWING- Rough ideas of what we want, we are open to sugestion so are looking for artistic input on part of the designer.

2,3,4,5,6,7,8 are all bag/ product designs we like.

Plain white bag image in photoshop you can use to present ideas.

Forza ,the font we use for our logo and most of our marketing material

High res logo file.

Kind regards

Gareth

Target Market(s)

Male / Females 25-45 years old

Industry/Entity Type

Fitness

Font styles to use
Other font styles liked:
• forza (attached) and posible other for tundra range and other text

Requirements
Must have
• 1. Logo (text) of VitalPradera.example.co (as attached) can be in blue or black but font/font sizes must be same as in attached file.
• 2. Text "TUNDRA RANGE"
• 3. 3 small logos/sign as indicated in "DRAWING" file and design brief

```html
<!DOCTYPE html>
<html lang="en">
<head>
<meta charset="utf-8">
<title>VitalPradera.example.co – Tundra Range bag</title>
<link rel="stylesheet" href="https://fonts.googleapis.com/css2?family=Titillium+Web:wght@700&family=Open+Sans:ital,wght@1,400;1,700&family=Roboto:wght@400;900&display=swap">
<style>
  :root {
    --blue-deep: #1f5ee8;
    --blue-mid: #3b7cf0;
    --blue-light: #5aaaf2;
    --blue-pale: #b5dcf9;
    --ink: #111111;
    --star: #f2c81b;
    --paper: #ffffff;
  }
  html, body {
    margin: 0;
    width: 1200px;
    height: 1000px;
    overflow: hidden;
    background: var(--paper);
  }
  .canvas {
    position: relative;
    width: 1200px;
    height: 1000px;
  }
  .bag-face {
    position: absolute;
    left: 300px;
    top: 30px;
    width: 600px;
    height: 940px;
  }
  .brand-name {
    font-family: "Titillium Web", sans-serif;
    font-weight: 700;
    fill: var(--paper);
    letter-spacing: 1px;
  }
  .feature-title { font-family: "Roboto", sans-serif; font-weight: 900; fill: var(--ink); font-size: 7px; }
  .feature-sub { font-family: "Roboto", sans-serif; font-weight: 400; fill: var(--ink); font-size: 3.6px; }
  .feature-es { font-family: "Roboto", sans-serif; font-weight: 400; fill: var(--paper); font-size: 2.2px; }
  .line-name { font-family: "Open Sans", sans-serif; font-style: italic; }
  .line-name .primary { font-weight: 700; fill: var(--blue-mid); font-size: 27px; }
  .line-name .secondary { font-weight: 400; fill: var(--ink); font-size: 15px; }
</style>
</head>
<body>
<main class="canvas">
  <svg class="bag-face" viewBox="0 0 300 470" xmlns="http://www.w3.org/2000/svg" aria-label="VitalPradera.example.co Tundra Range bag front">
    <defs>
      <linearGradient id="frameTone" x1="0" y1="0" x2="1" y2="1">
        <stop offset="0" stop-color="var(--blue-deep)"/>
        <stop offset="0.6" stop-color="var(--blue-light)"/>
        <stop offset="1" stop-color="var(--blue-pale)"/>
      </linearGradient>
    </defs>

    <!-- decorative frame area -->
    <g class="frame-decoration" role="img" aria-label="Blue tech-style frame decoration along the top and left edges">
      <rect x="0" y="0" width="300" height="18" fill="url(#frameTone)"/>
      <rect x="0" y="0" width="58" height="470" fill="url(#frameTone)"/>
    </g>

    <!-- brand band -->
    <rect class="brand-band" x="72" y="66" width="33" height="374" fill="var(--blue-deep)"/>
    <text class="brand-name" transform="translate(97,430) rotate(-90)" font-size="20" textLength="350" lengthAdjust="spacingAndGlyphs">VITALPRADERA.EXAMPLE.CO</text>

    <!-- feature marks -->
    <g class="feature" transform="translate(165,132)">
      <polygon points="4,0 5.2,2.8 8,3 5.8,5 6.5,8 4,6.4 1.5,8 2.2,5 0,3 2.8,2.8" fill="var(--star)"/>
      <text class="feature-title" x="12" y="7">Quality</text>
      <text class="feature-sub" x="20" y="11">Guaranteed</text>
      <polygon points="18,12 95,12 92,16 16,16" fill="var(--ink)"/>
      <text class="feature-es" x="20" y="15">Calidad Garantizada</text>
    </g>
    <g class="feature" transform="translate(165,166)">
      <polygon points="4,0 5.2,2.8 8,3 5.8,5 6.5,8 4,6.4 1.5,8 2.2,5 0,3 2.8,2.8" fill="var(--star)"/>
      <text class="feature-title" x="12" y="7">Imported</text>
      <text class="feature-sub" x="32" y="11">Ingredients</text>
      <polygon points="14,12 98,12 95,16 12,16" fill="var(--ink)"/>
      <text class="feature-es" x="16" y="15">Materias Primas Importadas</text>
    </g>
    <g class="feature" transform="translate(165,200)">
      <polygon points="4,0 5.2,2.8 8,3 5.8,5 6.5,8 4,6.4 1.5,8 2.2,5 0,3 2.8,2.8" fill="var(--star)"/>
      <text class="feature-title" x="12" y="7">Good</text>
      <text class="feature-title" x="12" y="15">Manufacturing</text>
      <text class="feature-sub" x="32" y="19">Practices</text>
      <polygon points="14,20 112,20 109,24 12,24" fill="var(--ink)"/>
      <text class="feature-es" x="16" y="23">Buenas Practicas de Manufactura</text>
    </g>

    <!-- line name -->
    <text class="line-name" x="130" y="420"><tspan class="primary">Tundra</tspan></text>
    <text class="line-name" x="176" y="440"><tspan class="secondary">Range</tspan></text>
  </svg>
</main>
</body>
</html>
```